Website Design for Kids

We need to redesign our site brightowl.net.
Current site was done long ago in Flash. We need to remove Flash and create a responsive site which can be viewed on phone, tablets as well as PC.
We are looking for a new fresh design. No elements from existing design need to be incorporated into new design.
The site is targeted for kids 7-12 years old.
Design should have attractive colors and it should be easy to navigate. It will be even better to provide one theme for boys and one for girls.
New site will have following features:
SHORT STORIES
Ability to display thumbnails of stories available. When user click a story it will play.
See http://brightowl.net/stories/index.asp to get an idea.
MOVIES
We have two moves, more to come. Users will be able to see thumbnails and watch trailers. To watch full movie they will be redirect to a Clipvane page where they can pay and watch.
See http://brightowl.net/Movies/ to get an idea.
PICTURE STORIES
This will feature short stories. When a story is clicked it will start playing. The stories will have picture and text, possibly audio too.
See http://brightowl.net/stories/stories.asp to get an idea.
AUDIO STORIES
Audio stories recorded from kids or adults will be played. Optional photo of the person who recorded story will be displayed. User will have option to select a story by clicking thumbnail of stories.
VIDEO STORIES
Like audio stories, user will be able to scroll though thumbnails of stories and play one. Short video 1-3 mins will be played.
- I have upgraded budget and added a few more simple requirements. Need to decide soon so please submit your designs asap.
Number of Pages Required
5+ page

```html
<!DOCTYPE html>
<html lang="en">
<head>
<meta charset="utf-8">
<title>BrightOwl – Stories for Kids</title>
<link rel="stylesheet" href="https://fonts.googleapis.com/css2?family=Alfa+Slab+One&family=Fredoka:wght@500&display=swap">
<style>
:root{
  --sky-top:#a9def6;
  --sky-low:#7cc6ea;
  --grass:#9cc94f;
  --grass-dark:#7aa83a;
  --frame:#2b94cc;
  --frame-dark:#1d78ad;
  --stage-top:#7fcfe4;
  --stage-low:#96d9ea;
  --white:#ffffff;
  --logo:#2a93c9;
  --short:#b5401f; --short-fill:#d88f7b;
  --movies:#ec5e29; --movies-fill:#eaa98f;
  --picture:#dc4670; --picture-fill:#e08fa6;
  --audio:#7b61ae; --audio-fill:#ab9ad3;
}
*{box-sizing:border-box;margin:0;padding:0}
html,body{width:1200px;height:852px;overflow:hidden}
body{position:relative;font-family:Arial,Helvetica,sans-serif;background:var(--sky-top)}
.scenery{position:absolute;inset:0;
  background:linear-gradient(180deg,var(--sky-top) 0%,var(--sky-low) 55%,var(--grass) 70%,var(--grass-dark) 82%,var(--grass) 100%)}
.kids{position:absolute;left:295px;top:48px;width:600px;height:195px;border-radius:80px 80px 20px 20px;
  background:linear-gradient(180deg,#d9955f 0%,#f1c9a0 100%)}
.logo-cloud{position:absolute;left:362px;top:185px;width:504px;height:160px;background:var(--white);
  border:3px solid var(--frame);border-radius:60px 70px 0 0;display:flex;align-items:center;justify-content:center;padding-bottom:28px}
.brand{font-family:"Fredoka",sans-serif;font-weight:500;font-size:66px;letter-spacing:1px;color:var(--logo);text-transform:uppercase}
.ribbon{position:absolute;top:358px;width:60px;height:52px;background:var(--frame-dark)}
.ribbon--left{left:62px;clip-path:polygon(0 100%,25% 50%,0 0,100% 0,100% 100%)}
.ribbon--right{left:1078px;clip-path:polygon(0 0,100% 0,75% 50%,100% 100%,0 100%)}
.board{position:absolute;left:110px;top:320px;width:980px;height:468px;background:var(--frame);border-radius:8px}
.stage{position:absolute;left:10px;top:56px;width:960px;height:370px;
  background:linear-gradient(180deg,var(--stage-top) 0%,var(--stage-low) 100%);
  border-bottom:2px dashed rgba(255,255,255,.8)}
.nav{position:absolute;left:93px;top:328px;width:1014px;height:48px;background:var(--frame);border-radius:6px;
  display:flex;align-items:center;justify-content:flex-start;gap:57px;padding-left:65px}
.nav a{font-family:"Alfa Slab One",serif;font-size:17px;color:var(--white);text-decoration:none;letter-spacing:.3px}
.card{position:absolute;top:452px;width:223px;height:248px;border:5px solid;border-radius:18px;text-align:center;color:var(--white)}
.card__icon{position:absolute;left:50%;top:-48px;width:112px;height:112px;margin-left:-56px;border-radius:50%;
  display:flex;align-items:center;justify-content:center}
.card__icon svg{width:72px;height:72px}
.card__title{font-family:"Alfa Slab One",serif;font-weight:400;font-size:17px;line-height:20px;margin-top:83px;letter-spacing:.3px}
.card__text{font-size:12.5px;line-height:15px;margin:9px auto 0;width:160px}
.card__button{position:absolute;left:50%;bottom:15px;width:114px;height:32px;margin-left:-57px;border-radius:6px;
  color:var(--white);font-size:13.5px;line-height:32px;text-decoration:none}
.card--audio .card__title{margin-top:103px}
.card--short{left:133px;border-color:var(--short);background:var(--short-fill)}
.card--short .card__icon,.card--short .card__button{background:var(--short)}
.card--movies{left:369px;border-color:var(--movies);background:var(--movies-fill)}
.card--movies .card__icon,.card--movies .card__button{background:var(--movies)}
.card--picture{left:610px;border-color:var(--picture);background:var(--picture-fill)}
.card--picture .card__icon,.card--picture .card__button{background:var(--picture)}
.card--audio{left:846px;border-color:var(--audio);background:var(--audio-fill)}
.card--audio .card__icon,.card--audio .card__button{background:var(--audio)}
</style>
</head>
<body>
<div class="scenery" role="img" aria-label="Cartoon sky with clouds and two rainbows, green rolling hills, trees, butterflies and a flower"></div>
<div class="kids" role="img" aria-label="Group of cheerful cartoon children leaning over the sign"></div>
<div class="logo-cloud"><span class="brand">BrightOwl</span></div>

<div class="ribbon ribbon--left"></div>
<div class="ribbon ribbon--right"></div>
<main class="board"><div class="stage" role="img" aria-label="Light blue sunburst backdrop"></div></main>

<nav class="nav">
  <a href="#">HOME</a>
  <a href="#">SHORT STORIES</a>
  <a href="#">MOVIES</a>
  <a href="#">PICTURE STORIES</a>
  <a href="#">AUDIO STORIES</a>
</nav>

<section class="card card--short">
  <div class="card__icon">
    <svg viewBox="0 0 72 72" fill="none" stroke="#f6d9cc" stroke-width="2.5" stroke-linejoin="round">
      <path d="M8 16 L8 58 Q22 52 35 58 L35 16 Q22 10 8 16Z"/>
      <path d="M64 16 L64 58 Q50 52 37 58 L37 16 Q50 10 64 16Z"/>
      <path d="M4 20 V62 H68 V20"/>
    </svg>
  </div>
  <h2 class="card__title">SHORT STORIES</h2>
  <p class="card__text">Check our audio stories byclicking below to liste to our audio stories.</p>
  <a class="card__button" href="#">check audio</a>
</section>

<section class="card card--movies">
  <div class="card__icon">
    <svg viewBox="0 0 72 72" fill="#f8d6c8">
      <circle cx="22" cy="18" r="12"/><circle cx="48" cy="14" r="13"/>
      <rect x="12" y="32" width="40" height="28" rx="4"/>
      <path d="M52 40 L66 32 V60 L52 52Z"/>
      <rect x="4" y="38" width="10" height="12"/>
    </svg>
  </div>
  <h2 class="card__title">MOVIES</h2>
  <p class="card__text">Check our audio stories byclicking below to liste to our audio stories.</p>
  <a class="card__button" href="#">check audio</a>
</section>

<section class="card card--picture">
  <div class="card__icon">
    <svg viewBox="0 0 72 72">
      <path fill="#f7d2dd" d="M6 22 H22 L27 14 H45 L50 22 H66 V60 H6Z"/>
      <circle cx="36" cy="40" r="14" fill="#dc4670"/><circle cx="36" cy="40" r="10" fill="#f7d2dd"/>
      <rect x="56" y="26" width="6" height="4" fill="#dc4670"/>
    </svg>
  </div>
  <h2 class="card__title">PICTURE STORIES</h2>
  <p class="card__text">Check our audio stories byclicking below to liste to our audio stories.</p>
  <a class="card__button" href="#">check audio</a>
</section>

<section class="card card--audio">
  <div class="card__icon">
    <svg viewBox="0 0 72 72" fill="none" stroke="#e6defa" stroke-width="4" stroke-linecap="round">
      <rect x="26" y="4" width="20" height="38" rx="10" fill="#e6defa" stroke="none"/>
      <path d="M18 30 Q18 50 36 50 Q54 50 54 30"/>
      <path d="M36 50 V64 M24 66 H48"/>
    </svg>
  </div>
  <h2 class="card__title">AUDIO STORIES</h2>
  <p class="card__text">Check our audio stories byclicking below to listen to our audio stories.</p>
  <a class="card__button" href="#">check audio</a>
</section>
</body>
</html>
```